PowerPoint template for Credit Card Processor

We need a powerpoint template for our new credit card processing company. Our goal is to sign up merchants to accept credit cards. We will be making presentations to merchants to get them to sign up for our services.

We already have a logo designed. We'd like to incorporate that logo and color scheme in the powerpoint template. The logo file is an illustrator file.

I generally like light colored backgrounds. Nothing too dark.

Industry/Entity Type

Credit Card

Requirements
Must have
• our logo

```html
<!DOCTYPE html>
<html lang="en">
<head>
<meta charset="utf-8">
<title>Slide Template – CardBridge.net</title>
<link rel="stylesheet" href="https://fonts.googleapis.com/css2?family=Arimo:wght@400;700&family=Carlito:wght@700&display=swap">
<style>
  :root {
    --slide-blue: #4f81bd;
    --accent-orange: #f79646;
    --ring-white: #ffffff;
    --text-white: #ffffff;
    --text-black: #000000;
    --brand-band: #0b4a72;
    --brand-dot: #6fd3f2;
  }
  * { margin: 0; padding: 0; box-sizing: border-box; }
  html, body {
    width: 1200px;
    height: 899px;
    overflow: hidden;
    background: var(--slide-blue);
  }
  .slide {
    position: relative;
    width: 1200px;
    height: 899px;
    background: var(--slide-blue);
    font-family: "Arimo", Arial, sans-serif;
  }
  .main-header {
    position: absolute;
    left: 38px;
    top: 48px;
    font-size: 50px;
    font-weight: 700;
    color: var(--text-white);
    letter-spacing: 0.5px;
  }
  .sub-header-primary {
    position: absolute;
    left: 42px;
    top: 124px;
    font-size: 41px;
    font-weight: 700;
    color: var(--text-black);
  }
  .sub-header-secondary {
    position: absolute;
    left: 42px;
    top: 179px;
    font-size: 29px;
    color: var(--text-black);
  }
  .topic {
    position: absolute;
    left: 65px;
    color: var(--text-white);
  }
  .topic-one { top: 246px; }
  .topic-two { top: 416px; }
  .topic-three { top: 588px; }
  .topic-title {
    font-size: 30px;
    font-weight: 700;
    line-height: 36px;
  }
  .topic-list {
    list-style: none;
    font-size: 28px;
    line-height: 35.5px;
  }
  .topic-list li {
    position: relative;
    padding-left: 37px;
  }
  .topic-list li::before {
    content: "•";
    position: absolute;
    left: 0;
    font-size: 22px;
  }
  .figure-chain {
    position: absolute;
    left: 0;
    top: 0;
  }
  .figure-label {
    font-family: "Carlito", Calibri, sans-serif;
    font-weight: 700;
    fill: var(--text-white);
    text-anchor: middle;
    dominant-baseline: central;
  }
  .brand-band {
    position: absolute;
    left: 574px;
    top: 806px;
    width: 620px;
    height: 93px;
    background: var(--brand-band);
    display: flex;
    align-items: center;
    padding-left: 32px;
    gap: 22px;
  }
  .brand-dot {
    width: 56px;
    height: 56px;
    border-radius: 50%;
    background: var(--brand-dot);
  }
  .brand-name {
    font-size: 58px;
    font-weight: 400;
    color: var(--text-white);
    letter-spacing: 0.5px;
  }
</style>
</head>
<body>
  <main class="slide">
    <h1 class="main-header">MAIN HEADER</h1>
    <h2 class="sub-header-primary">Sub header 1</h2>
    <p class="sub-header-secondary">Sub header 2</p>

    <section class="topic topic-one">
      <h3 class="topic-title">Plain Text</h3>
      <ul class="topic-list">
        <li>Line 1</li>
        <li>Line 2</li>
        <li>Line 3</li>
      </ul>
    </section>

    <section class="topic topic-two">
      <h3 class="topic-title">Plain Text</h3>
      <ul class="topic-list">
        <li>Line 1</li>
        <li>Line 2</li>
        <li>Line 3</li>
      </ul>
    </section>

    <section class="topic topic-three">
      <h3 class="topic-title">Plain Text</h3>
      <ul class="topic-list">
        <li>Line 1</li>
        <li>Line 2</li>
        <li>Line 3</li>
      </ul>
    </section>

    <svg class="figure-chain" width="1200" height="899" viewBox="0 0 1200 899" aria-label="Key figures">
      <line x1="935" y1="356" x2="935" y2="630" stroke="var(--ring-white)" stroke-width="3.5"/>
      <circle cx="931" cy="223" r="135" fill="var(--accent-orange)" stroke="var(--ring-white)" stroke-width="3.5"/>
      <circle cx="931" cy="480" r="70" fill="var(--accent-orange)" stroke="var(--ring-white)" stroke-width="3.5"/>
      <circle cx="936" cy="671" r="43" fill="var(--accent-orange)" stroke="var(--ring-white)" stroke-width="3.5"/>
      <text class="figure-label" x="931" y="223" font-size="43">Figures</text>
      <text class="figure-label" x="931" y="480" font-size="54">%</text>
      <text class="figure-label" x="936" y="671" font-size="32">N</text>
    </svg>

    <footer class="brand-band">
      <span class="brand-dot"></span>
      <span class="brand-name">CardBridge.net</span>
    </footer>
  </main>
</body>
</html>
```